Property Finance Company - Orin Ventures Limited

Background: Orin Ventures Group Limited is a private property finance company. Orin Ventures Group has capital to directly fund first mortgage, mezzanine and preferred equity financing. We also acquire performing, sub-performing and distressed debt.

Orin Ventures' management philosophy emphasises expertise, innovation, wisdom, honesty and competitiveness. Orin Ventures are not finance brokers - we provide debt funding to the commercial property and residential development sectors. Our process is built from experience and cumutavely Orin Ventures' Directors have in excess of 60 years wisdom.

The aim of the website will be to increase brand awareness, provide clients with comfort around our level of skill and background on who we are, generate more sales, and provide examples of projects that we have funded.

The website is a new product launch, and we need to use our Orin Ventures logo that has just been designed. We like a dark background, and either black/silver/grey/ jade green, or black/gold/jade green colours.

Our unique advantages are that we have fast turnaround times, we can solve clients funding problems and we know what we are doing. Our target audience will be viewing the website on both desktop and mobile devices.

We would like to have the following pages:

Home
About
Team
Services
Project Experience
Contact

Competitors Website: http://www.tarvelo.com/

We would also like to have the option of video footage in our website, as you can see in our competitors website.

Overall we want a really slick, elegant but modern website that is better than www.tarvelo.com

Target Market(s)

Finance borrowers, property developers, accountants, lawyers, businesspeople, high net worth people

Industry/Entity Type

Finance

Requirements
Must have
• Please see project description
Nice to have
Should not have

```html
<!DOCTYPE html>
<html lang="en">
<head>
<meta charset="utf-8">
<title>Orin Ventures Group — Property Finance</title>
<link href="https://fonts.googleapis.com/css2?family=Libre+Franklin:wght@400;500;600;700&display=swap" rel="stylesheet">
<style>
:root{
  --jade:#12a86b;
  --ink:#1d1d1f;
  --text:#2b2b2b;
  --muted:#8a8a8a;
  --line:#dcdde2;
  --soft:#f3f4f8;
  --white:#ffffff;
  --night:#231f20;
  --night-line:#3b3637;
}
*{box-sizing:border-box;margin:0;padding:0}
html,body{width:1200px;height:3175px;overflow:hidden}
body{font-family:"Libre Franklin",Arial,sans-serif;color:var(--text);background:var(--white);position:relative}
a{color:inherit;text-decoration:none}
.abs{position:absolute}
.arrow::after{content:" \2192"}

/* hero */
.hero{position:absolute;left:0;top:0;width:1200px;height:643px;overflow:hidden}
.hero-media{position:absolute;inset:0;background:linear-gradient(120deg,#5b6466 0%,#7a8688 35%,#4a5557 65%,#2f3839 100%)}
.hero-shade{position:absolute;inset:0;background:linear-gradient(90deg,rgba(20,24,26,.55) 0%,rgba(20,24,26,.15) 55%,rgba(20,24,26,.25) 100%)}
.brand{display:flex;align-items:center;gap:10px;color:var(--white);font-weight:600;font-size:17px;letter-spacing:.5px}
.brand-dot{width:22px;height:22px;border-radius:50%;border:2px solid currentColor}
.hero .brand{position:absolute;left:127px;top:52px}
.menu{position:absolute;left:1090px;top:52px;width:32px}
.menu span{display:block;height:2px;background:var(--white);margin-bottom:8px}
.hero-copy{position:absolute;left:127px;top:246px;color:var(--white);width:300px}
.hero-kicker{font-size:14px;font-weight:500}
.hero-title{font-size:31px;font-weight:600;line-height:1.12;margin-top:8px}
.hero-sub{font-size:13px;font-weight:500;line-height:1.4;margin-top:14px}
.hero-link{display:block;font-size:12px;font-weight:500;margin-top:28px}
.watch{position:absolute;left:127px;top:550px;display:flex;align-items:center;gap:12px;color:var(--white);font-size:13px;font-weight:500}
.scroll{position:absolute;left:590px;top:540px}

/* section scaffolding */
.section{position:absolute;left:0;width:1200px}
.section-title{position:absolute;left:127px;font-size:30px;font-weight:500;color:var(--ink)}
.vline{position:absolute;left:381px;width:1px;background:var(--line)}
.hline{position:absolute;left:76px;width:1048px;height:1px;background:var(--line)}
.more{position:absolute;right:155px;font-size:12px;font-weight:500;color:var(--ink)}
.more.green{color:var(--jade);text-decoration:underline}

/* about */
.about{top:643px;height:485px;background:var(--white)}
.about .section-title{top:58px;line-height:1.2}
.about-tag{position:absolute;left:127px;top:186px;width:230px;font-size:15px;font-weight:600;line-height:1.4;color:var(--ink)}
.about-body{position:absolute;left:434px;top:62px;width:410px}
.lead{font-size:14px;font-weight:500;line-height:1.45;color:var(--ink)}
.small{font-size:12px;line-height:1.65;color:var(--muted);margin-top:26px}
.lead.mt{margin-top:24px}
.lead em{font-style:normal;color:var(--jade)}
.btn-jade{display:inline-block;margin-top:50px;background:var(--jade);color:var(--white);font-size:12px;font-weight:500;padding:11px 24px}
.about-photo{position:absolute;left:918px;width:282px;height:242px}

/* services */
.services{top:1128px;height:484px;background:var(--soft)}
.service{position:absolute;top:149px;width:285px}
.service h3{font-size:15px;font-weight:600;color:var(--ink)}
.service p{font-size:12px;line-height:1.62;color:var(--muted);margin-top:22px}
.service .read{position:absolute;top:244px;left:0;font-size:12px;font-weight:500;color:var(--ink);white-space:nowrap}
.service .read.active{color:var(--jade);text-decoration:underline}

/* projects */
.projects{top:1612px;height:642px;background:var(--white)}
.project{position:absolute;overflow:hidden;color:var(--white)}
.project .shade{position:absolute;inset:0;background:linear-gradient(0deg,rgba(0,0,0,.5),rgba(0,0,0,0) 55%)}
.project .label{position:absolute;left:24px;bottom:22px}
.project h4{font-size:16px;font-weight:600}
.project small{display:block;font-size:11px;margin-top:3px}
.project.featured{background:var(--jade)}
.project.featured .label{top:22px;bottom:auto}
.project.featured p{font-size:13px;line-height:1.45;margin-top:22px}
.project.featured .read{display:block;font-size:12px;font-weight:500;margin-top:22px}

/* team */
.team{top:2254px;height:567px;background:var(--soft)}
.dots{position:absolute;left:994px;top:140px;display:flex;gap:8px}
.dots i{width:8px;height:8px;border-radius:50%;background:#c2c4ca}
.dots i.on{background:var(--jade)}
.member{position:absolute;top:156px;width:275px;background:var(--white)}
.member .portrait{height:214px}
.member .name{height:64px;text-align:center;padding-top:14px}
.member strong{display:block;font-size:15px;font-weight:600;color:var(--ink)}
.member span{display:block;font-size:11px;color:var(--muted);margin-top:5px}
.member.active{box-shadow:0 10px 30px rgba(0,0,0,.12)}
.member.active .name{background:var(--jade)}
.member.active strong,.member.active span{color:var(--white)}
.btn-outline{position:absolute;left:535px;top:467px;width:132px;height:34px;border:1.5px solid var(--jade);background:var(--white);font-size:12px;font-weight:500;color:var(--ink);text-align:center;line-height:31px}

/* contact */
.contact{top:2821px;height:354px;background:var(--night);color:var(--white)}
.contact .section-title{color:var(--white);top:52px}
.contact .vline,.contact .hline{background:var(--night-line)}
.contact .brand{position:absolute;left:127px;top:200px;font-size:18px}
.col{position:absolute;top:166px}
.col h5{font-size:14px;font-weight:600}
.col p{font-size:12px;line-height:1.6;color:#b9b6b6;margin-top:28px}
.phone{font-size:20px;color:#d8d6d6;margin-top:20px}
.mail{font-size:12px;color:#b9b6b6;margin-top:4px}
.mail a{color:var(--jade);text-decoration:underline}
.socials{display:flex;gap:8px;margin-top:24px}
.socials i{width:28px;height:28px;border-radius:50%;background:#8d8a8a}
.socials i.on{background:var(--jade)}
.copy{position:absolute;left:127px;top:310px;font-size:12px;color:#b9b6b6}
.copy a{color:var(--jade);text-decoration:underline}
.to-top{position:absolute;left:1021px;top:305px}
</style>
</head>
<body>

<header class="hero">
  <div class="hero-media" role="img" aria-label="Business team meeting around a table in a bright modern office"></div>
  <div class="hero-shade"></div>
  <div class="brand"><span class="brand-dot"></span>Orin Ventures Group</div>
  <div class="menu"><span></span><span></span><span></span></div>
  <div class="hero-copy">
    <div class="hero-kicker">Orin Ventures Group</div>
    <h1 class="hero-title">We Provide Debt Funding</h1>
    <p class="hero-sub">to the commercial property and residential development sectors</p>
    <a class="hero-link arrow" href="#">Explore More</a>
  </div>
  <a class="watch" href="#">
    <svg width="30" height="30" viewBox="0 0 30 30"><circle cx="15" cy="15" r="13.5" fill="none" stroke="#fff" stroke-width="2"/><path d="M12 9.5 L21 15 L12 20.5Z" fill="#fff"/></svg>
    Watch Video
  </a>
  <svg class="scroll" width="20" height="34" viewBox="0 0 20 34"><rect x="1" y="1" width="18" height="32" rx="9" fill="none" stroke="#fff" stroke-width="2"/><rect x="8.5" y="8" width="3" height="8" rx="1.5" fill="#fff"/></svg>
</header>

<section class="section about">
  <h2 class="section-title">About<br>Company</h2>
  <div class="vline" style="top:0;height:485px"></div>
  <div class="abs" style="left:76px;top:155px;width:305px;height:1px;background:var(--line)"></div>
  <p class="about-tag">Orin Ventures Group Limited is a Private Property Finance Company.</p>
  <div class="about-body">
    <p class="lead">Orin Ventures Group has capital to directly fund first mortgage, mezzanine and preferred equity financing. We also acquire performing, sub-performing and distressed debt.</p>
    <p class="small">Orin Ventures' management philosophy emphasises expertise, innovation, wisdom, honesty and competitiveness. Orin Ventures are not finance brokers - we provide debt funding to the commercial property and residential development sectors.</p>
    <p class="lead mt">Our process is built from experience and cumutavely <em>Orin Ventures' Directors have in excess of 60 years wisdom.</em></p>
    <a class="btn-jade" href="#">Discover More</a>
  </div>
  <div class="about-photo" style="top:0;background:linear-gradient(135deg,#dfe3e6,#9aa3a8)" role="img" aria-label="Two colleagues discussing work at a desk"></div>
  <div class="about-photo" style="top:243px;background:linear-gradient(135deg,#6c7478,#39424a)" role="img" aria-label="Team gathered around a laptop"></div>
</section>

<section class="section services">
  <h2 class="section-title" style="top:60px">Our Services</h2>
  <div class="vline" style="top:0;height:120px"></div>
  <div class="hline" style="top:120px"></div>
  <a class="more arrow" style="top:84px" href="#">View All Services</a>
  <article class="service" style="left:127px">
    <h3>Development Finance</h3>
    <p>There are many variations of passages of Lorem Ipsum available, but the majority have suffered alteration in some form, by injected humour, or randomised words which don't look even slightly believable.<br>If you are going to use a passage of Lorem Ipsum...</p>
    <a class="read arrow" href="#">Read More</a>
  </article>
  <article class="service" style="left:434px">
    <h3>Bridging Finance</h3>
    <p>There are many variations of passages of Lorem Ipsum available, but the majority have suffered alteration in some form, by injected humour, or randomised words which don't look even slightly believable.<br>If you are going to use a passage of Lorem Ipsum...</p>
    <a class="read active arrow" href="#">Read More</a>
  </article>
  <article class="service" style="left:739px">
    <h3>Bank Finance</h3>
    <p>There are many variations of passages of Lorem Ipsum available, but the majority have suffered alteration in some form, by injected humour, or randomised words which don't look even slightly believable.<br>If you are going to use a passage of Lorem Ipsum...</p>
    <a class="read arrow" href="#">Read More</a>
  </article>
</section>

<section class="section projects">
  <h2 class="section-title" style="top:64px">Our Projects</h2>
  <div class="vline" style="top:0;height:119px"></div>
  <div class="hline" style="top:119px"></div>
  <a class="more green arrow" style="top:84px" href="#">View All Projects</a>
  <div class="project" style="left:127px;top:153px;width:283px;height:201px">
    <div class="abs" style="inset:0;background:linear-gradient(160deg,#d9dde0,#8c969b 60%,#5d6b55)" role="img" aria-label="White modern residential building"></div>
    <div class="shade"></div>
    <div class="label"><h4>Queen Residences</h4><small>Centuries</small></div>
  </div>
  <div class="project featured" style="left:434px;top:153px;width:611px;height:201px">
    <div class="label">
      <h4>Commercial Offices</h4><small>Centuries</small>
      <p>$14,000,000 low prise office building.<br>15 units.<br>Completed October 2016</p>
      <a class="read arrow" href="#">Read More</a>
    </div>
  </div>
  <div class="project" style="left:127px;top:377px;width:588px;height:201px">
    <div class="abs" style="inset:0;background:linear-gradient(90deg,#3d4650,#7f8a92 55%,#4e86c0 80%,#9cc3e6)" role="img" aria-label="Apartment facade with balconies against blue sky"></div>
    <div class="shade"></div>
    <div class="label"><h4>Aria Apartments</h4><small>Centuries</small></div>
  </div>
  <div class="project" style="left:740px;top:377px;width:305px;height:201px">
    <div class="abs" style="inset:0;background:linear-gradient(160deg,#aebfd0,#6e7f8f 60%,#4a5866)" role="img" aria-label="Glass commercial tower seen from below"></div>
    <div class="shade"></div>
    <div class="label"><h4>Commercial Building</h4><small>Centuries</small></div>
  </div>
</section>

<section class="section team">
  <h2 class="section-title" style="top:62px">Our Team</h2>
  <div class="vline" style="top:0;height:121px"></div>
  <div class="hline" style="top:121px"></div>
  <div class="dots"><i></i><i class="on"></i><i></i><i></i></div>
  <div class="member" style="left:127px">
    <div class="portrait" style="background:linear-gradient(160deg,#b9b3ad,#8a7f76)" role="img" aria-label="Portrait of team member"></div>
    <div class="name"><strong>Aldo Verran</strong><span>Wendell</span></div>
  </div>
  <div class="member active" style="left:451px">
    <div class="portrait" style="background:linear-gradient(160deg,#f2f2f2,#d8cbb8)" role="img" aria-label="Portrait of team member"></div>
    <div class="name"><strong>Mira Castell</strong><span>Wendell</span></div>
  </div>
  <div class="member" style="left:772px">
    <div class="portrait" style="background:linear-gradient(160deg,#ececec,#9a9390)" role="img" aria-label="Portrait of team member"></div>
    <div class="name"><strong>Tobin Hale</strong><span>Wendell</span></div>
  </div>
  <a class="btn-outline" href="#">View All Team</a>
</section>

<footer class="section contact">
  <h2 class="section-title">Contact Us</h2>
  <div class="vline" style="top:0;height:120px"></div>
  <div class="hline" style="top:120px"></div>
  <a class="more green arrow" style="top:80px" href="#">Get Direction</a>
  <div class="brand"><span class="brand-dot"></span>Orin Ventures Group</div>
  <div class="col" style="left:434px">
    <h5>Address:</h5>
    <p>4410 Corran Avenue,<br>Halden, KT 20418</p>
  </div>
  <div class="col" style="left:677px">
    <h5>Call Us:</h5>
    <div class="phone">555 - 302 - 1184</div>
    <div class="mail"><a href="#">E-mail</a> Us.</div>
  </div>
  <div class="col" style="left:912px">
    <h5>Get Social:</h5>
    <div class="socials"><i></i><i class="on"></i><i></i><i></i></div>
  </div>
  <div class="hline" style="top:283px"></div>
  <p class="copy">© 2017 <a href="#">Orin Ventures Group.</a> All Rights Reserved</p>
  <svg class="to-top" width="24" height="24" viewBox="0 0 24 24"><circle cx="12" cy="12" r="12" fill="var(--jade)"/><path d="M12 7 L17 13 H13.5 V17 H10.5 V13 H7Z" fill="#231f20"/></svg>
</footer>

</body>
</html>
```